GUILD Book Cover

I need ideas for my new book cover. I currently have 2 possible titles. 1.) The Hard Won Guild of Desk Craft 2.) Desk Craft Worth, Yes Truly! The book covers real life experiences & examples of how to 1.) understand GUILD & 2.) Best practices around implementation. GUILD = Information Technology Service Management. The final design should sell VALUE! I'm a great believer in choice is not about choice it's about value or perceived value. I need to capture this on the cover.

Information Technology

```html
<!DOCTYPE html>
<html lang="en">
<head>
<meta charset="utf-8">
<title>The Hard Won Guild of Desk Craft – Book Cover</title>
<link rel="stylesheet" href="https://fonts.googleapis.com/css2?family=Anton&family=Arimo:wght@400&display=swap">
<style>
  :root {
    --night-top: #4a4d6e;
    --night-mid: #2a2b40;
    --night-deep: #050509;
    --value-yellow: #fff200;
    --ink: #050505;
    --paper: #ffffff;
    --band: rgba(235, 236, 242, 0.82);
  }
  html, body {
    margin: 0;
    padding: 0;
    width: 927px;
    height: 1200px;
    overflow: hidden;
    background: var(--night-deep);
  }
  .cover {
    position: relative;
    width: 927px;
    height: 1200px;
    overflow: hidden;
  }
  .cover__artwork {
    position: absolute;
    inset: 0;
    background:
      radial-gradient(ellipse 300px 40px at 462px 945px, rgba(238,240,255,0.85), rgba(238,240,255,0) 100%),
      radial-gradient(ellipse 470px 280px at 470px 450px, rgba(245,246,255,0.9), rgba(200,204,235,0.35) 60%, rgba(200,204,235,0) 100%),
      radial-gradient(ellipse 60px 320px at 462px 750px, rgba(220,224,250,0.6), rgba(220,224,250,0) 100%),
      linear-gradient(180deg, var(--night-top) 0%, var(--night-mid) 55%, var(--night-deep) 85%, var(--night-deep) 100%);
  }
  .cover__layout {
    position: absolute;
    inset: 0;
  }
  .frame { fill: none; stroke: var(--paper); stroke-width: 1.5; }
  .masthead {
    font-family: "Anton", "Arial Narrow", sans-serif;
    font-size: 300px;
    fill: var(--value-yellow);
  }
  .band { fill: var(--band); }
  .band-label {
    font-family: "Anton", "Arial Narrow", sans-serif;
    font-size: 34px;
    fill: var(--ink);
  }
  .guild-line {
    font-family: "Arimo", Arial, sans-serif;
    font-size: 41px;
    fill: var(--ink);
  }
  .book-title {
    font-family: "Anton", "Arial Narrow", sans-serif;
    font-size: 200px;
    fill: var(--ink);
    stroke: var(--value-yellow);
    stroke-width: 8px;
    paint-order: stroke;
    stroke-linejoin: round;
  }
  .tagline {
    font-family: "Arimo", Arial, sans-serif;
    font-size: 41px;
    fill: var(--paper);
  }
  .blurb {
    font-family: "Arimo", Arial, sans-serif;
    font-size: 28px;
    fill: var(--paper);
  }
  .web-address {
    font-family: "Arimo", Arial, sans-serif;
    font-size: 24px;
    fill: var(--value-yellow);
  }
</style>
</head>
<body>
  <main class="cover">
    <div class="cover__artwork" role="img" aria-label="Glowing tree made of scattered light particles against a dark night sky, lit from below"></div>

    <svg class="cover__layout" width="927" height="1200" viewBox="0 0 927 1200">
      <rect class="frame" x="42" y="40" width="845" height="1115"/>

      <text class="masthead" x="459" y="371" text-anchor="middle" textLength="621" lengthAdjust="spacingAndGlyphs">GUILD</text>

      <rect class="band" x="0" y="202" width="927" height="91"/>
      <text class="band-label" x="463" y="257" text-anchor="middle" textLength="655" lengthAdjust="spacingAndGlyphs">INFORMATION TECHNOLOGY SERVICE MANAGEMENT</text>

      <text class="guild-line" x="459" y="491" text-anchor="middle">The Hard Won Guild of</text>

      <text class="book-title" x="462" y="716" text-anchor="middle" textLength="420" lengthAdjust="spacingAndGlyphs">DESK</text>
      <text class="book-title" x="462" y="928" text-anchor="middle" textLength="500" lengthAdjust="spacingAndGlyphs">CRAFT</text>

      <text class="tagline" x="460" y="1022" text-anchor="middle">Desk Craft Worth, Yes Truly!</text>
      <text class="blurb" x="464" y="1062" text-anchor="middle">The book covers real life experiences &amp; examples</text>
      <text class="web-address" x="470" y="1119" text-anchor="middle">www.deskcraftguild.com</text>
    </svg>
  </main>
</body>
</html>
```